Lanterne architecture business cards

We are a new company based in New Zealand. We Specialize in High end Luxury Residential Architecture.

Every home is bespoke and is designed to each clients individual requirements and needs.

I like to design buildings that inspire people through light and form while offering a high level of comfort and usability.

Lines of sight, proportion and balance are fundamental to the spaces I create.
Updates

August 5th is current deadline - Today's date is the 13th of August.

Target Market(s)

New Zealanders who want a custom individual home design, typically 30-65 year old males and females

Industry/Entity Type

Architecture

Contact Information for Business Card

Director - Derek Tolson
Contact Number - 0279164073
Email - info@lanternearchitecture-example.co.nz
Webstie - www.lanternearchitecture-example.co.nz
Social Media - @lanternearchitecture

Font styles to use
Sans Serif

Requirements
Must have
• Logo (Both Sides)
Website
Email
Contact Number
Social Media

Nice to have
• Texture
Should not have
• More than 3 colours - typically I would've thought 2 would be good to match the logo.

```html
<!DOCTYPE html>
<html lang="en">
<head>
<meta charset="utf-8">
<title>Lanterne Architecture — Business Cards</title>
<link href="https://fonts.googleapis.com/css2?family=Jost:wght@300;400;500;600&display=swap" rel="stylesheet">
<style>
  :root {
    --backdrop: #ece8e8;
    --ink: #111111;
    --paper: #ffffff;
    --foil-light: #fbfbfb;
    --foil-mid: #e6e8e8;
    --foil-dark: #d3d6d6;
    --slate: #5d6868;
    --muted: #8a8f8f;
  }
  * { margin: 0; padding: 0; box-sizing: border-box; }
  html, body { width: 1200px; height: 960px; overflow: hidden; }
  body {
    background: var(--backdrop);
    font-family: "Jost", sans-serif;
    color: var(--ink);
    position: relative;
  }
  .card {
    position: absolute;
    left: 257px;
    width: 667px;
    height: 381px;
    overflow: hidden;
  }
  .foil {
    background:
      radial-gradient(ellipse at 70% 20%, var(--foil-light) 0%, transparent 55%),
      linear-gradient(135deg, var(--foil-mid) 0%, var(--foil-light) 40%, var(--foil-dark) 75%, var(--foil-light) 100%);
  }

  /* Front card */
  .card-front { top: 49px; }
  .front-brand {
    position: absolute;
    left: 0; right: 0; top: 36px;
    display: flex; flex-direction: column; align-items: center;
    transform: translateX(26px);
  }
  .brand-ring {
    width: 62px; height: 62px;
    border: 7px solid var(--ink);
    border-radius: 50%;
  }
  .brand-name {
    margin-top: 48px;
    font-size: 26px;
    font-weight: 300;
    letter-spacing: 0.5em;
    margin-right: -0.5em;
    text-transform: uppercase;
  }
  .brand-tag {
    margin-top: 6px;
    font-size: 10px;
    font-weight: 300;
    letter-spacing: 2.7em;
    margin-right: -2.7em;
    text-transform: uppercase;
  }
  .front-rule {
    position: absolute; left: 0; right: 0;
    top: 300px; height: 5px;
    background: var(--ink);
  }
  .front-band {
    position: absolute; left: 0; right: 0;
    top: 324px; bottom: 0;
    background: var(--ink);
    display: flex; justify-content: center;
    padding-top: 7px;
  }
  .front-url {
    color: var(--paper);
    font-size: 14px;
    font-weight: 300;
    transform: translateX(26px);
  }

  /* Back card */
  .card-back { top: 507px; }
  .back-edge-mark {
    position: absolute; left: 0; top: 338px;
    width: 14px; height: 8px;
    background: var(--ink);
  }
  .back-panel {
    position: absolute; left: 14px; top: 0;
    width: 344px; height: 100%;
    background: var(--ink);
    color: var(--paper);
  }
  .back-brand {
    position: absolute; left: 0; right: 0; top: 129px;
    display: flex; flex-direction: column; align-items: center;
    transform: translateX(-6px);
  }
  .back-brand .brand-ring {
    width: 34px; height: 34px;
    border: 4px solid var(--paper);
  }
  .back-brand .brand-name {
    margin-top: 26px;
    font-size: 17px;
    letter-spacing: 0.55em;
    margin-right: -0.55em;
  }
  .back-brand .brand-tag {
    margin-top: 3px;
    font-size: 6px;
    letter-spacing: 2.4em;
    margin-right: -2.4em;
    color: var(--muted);
  }
  .contact {
    position: absolute; left: 390px; top: 0; right: 0; bottom: 0;
  }
  .person-name {
    position: absolute; top: 52px;
    font-size: 26px; font-weight: 600;
    letter-spacing: 0.01em;
    text-transform: uppercase;
  }
  .person-role {
    position: absolute; top: 86px;
    font-size: 18px; font-weight: 600;
    color: var(--slate);
  }
  .contact-list { position: absolute; top: 179px; list-style: none; }
  .contact-item {
    display: flex; align-items: center;
    height: 24px;
    font-size: 13.5px;
  }
  .contact-item:first-child { font-size: 16px; margin-bottom: 4px; }
  .contact-icon {
    width: 14px; margin-right: 11px;
    display: flex; justify-content: center;
    font-weight: 600; font-size: 16px;
  }
  .social {
    position: absolute; top: 304px; left: 23px;
  }
  .social-handle { font-size: 14.5px; }
  .social-dots {
    display: flex; gap: 17px;
    margin-top: 6px; margin-left: 17px;
  }
  .social-dots span {
    width: 12px; height: 12px; border-radius: 50%;
    background: var(--slate);
  }
</style>
</head>
<body>

  <section class="card card-front foil" aria-label="Front of business card">
    <div class="front-brand">
      <div class="brand-ring"></div>
      <div class="brand-name">Lanterne</div>
      <div class="brand-tag">Architecture</div>
    </div>
    <div class="front-rule"></div>
    <div class="front-band">
      <span class="front-url">www.lanternearchitecture-example.co.nz</span>
    </div>
  </section>

  <section class="card card-back foil" aria-label="Back of business card">
    <div class="back-edge-mark"></div>
    <div class="back-panel">
      <div class="back-brand">
        <div class="brand-ring"></div>
        <div class="brand-name">Lanterne</div>
        <div class="brand-tag">Architecture</div>
      </div>
    </div>

    <div class="contact">
      <h1 class="person-name">Derek Tolson</h1>
      <p class="person-role">Director</p>

      <ul class="contact-list">
        <li class="contact-item">
          <span class="contact-icon">
            <svg width="10" height="16" viewBox="0 0 10 16"><rect x="1" y="1" width="8" height="14" rx="1.5" fill="none" stroke="#111" stroke-width="1.8"/><line x1="4" y1="12.5" x2="6" y2="12.5" stroke="#111" stroke-width="1.4"/></svg>
          </span>
          0279164073
        </li>
        <li class="contact-item">
          <span class="contact-icon">@</span>
          info@lanternearchitecture-example.co.nz
        </li>
        <li class="contact-item">
          <span class="contact-icon">
            <svg width="14" height="14" viewBox="0 0 14 14" fill="none" stroke="#111" stroke-width="1.3"><circle cx="7" cy="7" r="6"/><ellipse cx="7" cy="7" rx="2.6" ry="6"/><line x1="1" y1="7" x2="13" y2="7"/><line x1="2" y1="4" x2="12" y2="4"/><line x1="2" y1="10" x2="12" y2="10"/></svg>
          </span>
          www.lanternearchitecture-example.co.nz
        </li>
      </ul>

      <div class="social">
        <div class="social-handle">@lanternearchitecture</div>
        <div class="social-dots" aria-hidden="true">
          <span></span><span></span><span></span><span></span>
        </div>
      </div>
    </div>
  </section>

</body>
</html>
```